Dalton Power Supply, Inc. Business Card Design

We are an Electrical Distributor looking for a Modern, Professional Business Card design.

Target Market(s)

Residential Commercial Industrial

Industry/Entity Type

Electrical

Contact Information for Business Card

Dalton Power Supply, Inc.
418 Maple Ridge Lane
Brookvale, NC 27514
555-214-7630
555-214-8842 Fax
daltonpower@brightmail-example.net

```html
<!DOCTYPE html>
<html lang="en">
<head>
<meta charset="utf-8">
<title>Dalton Power Supply, Inc. — Business Card</title>
<link href="https://fonts.googleapis.com/css2?family=Open+Sans:wght@400;600;700&display=swap" rel="stylesheet">
<style>
  :root {
    --stage: #e9e7e4;
    --card-dark: #111111;
    --card-light: #ffffff;
    --orange: #ff5a00;
    --orange-light: #ff8a1a;
    --ink: #1a1a1a;
    --white: #ffffff;
  }
  * { box-sizing: border-box; margin: 0; padding: 0; }
  html, body { width: 1200px; height: 900px; overflow: hidden; }
  body {
    background: var(--stage);
    font-family: "Open Sans", Arial, sans-serif;
    position: relative;
  }
  .card {
    position: absolute;
    left: 250px;
    width: 700px;
    height: 400px;
    box-shadow: 0 6px 18px rgba(0,0,0,0.18);
    overflow: hidden;
  }
  .card--front { top: 40px; background: var(--card-dark); }
  .card--back { top: 470px; background: var(--card-light); }

  .front-name {
    position: absolute;
    inset: 0;
    display: flex;
    align-items: center;
    justify-content: center;
    gap: 16px;
    color: var(--white);
    font-weight: 600;
    font-size: 40px;
    letter-spacing: 1px;
  }
  .mark-dot {
    width: 22px; height: 22px; border-radius: 50%;
    background: var(--white);
  }

  .corner-tab { position: absolute; left: 0; top: 0; }
  .short-name {
    position: absolute;
    left: 100px; top: 34px;
    color: var(--orange);
    font-weight: 700;
    font-size: 26px;
    letter-spacing: 0.5px;
  }
  .contact {
    position: absolute;
    left: 44px; top: 168px;
    color: var(--ink);
    font-size: 19px;
    line-height: 26px;
    list-style: none;
  }
  .contact li { display: flex; align-items: center; gap: 10px; }
  .contact .icon { width: 14px; height: 14px; flex: none; }
  .contact .plain { padding-left: 0; }

  .back-name {
    position: absolute;
    right: 40px; top: 175px;
    width: 300px;
    text-align: center;
    color: var(--orange);
    font-weight: 600;
    font-size: 30px;
    line-height: 38px;
  }
  .bottom-band { position: absolute; left: 0; bottom: 0; }
</style>
</head>
<body>
  <section class="card card--front" aria-label="Card front">
    <div class="front-name"><span class="mark-dot"></span>Dalton Power Supply, Inc.</div>
  </section>

  <section class="card card--back" aria-label="Card back">
    <svg class="corner-tab" width="95" height="60" viewBox="0 0 95 60">
      <defs>
        <linearGradient id="tabFill" x1="0" y1="0" x2="1" y2="0">
          <stop offset="0" stop-color="var(--orange)"/>
          <stop offset="1" stop-color="var(--orange-light)"/>
        </linearGradient>
      </defs>
      <polygon points="0,8 62,8 38,58 0,58" fill="url(#tabFill)"/>
      <polygon points="70,8 88,8 64,58 46,58" fill="url(#tabFill)"/>
    </svg>
    <div class="short-name">DALTON</div>

    <ul class="contact">
      <li class="plain">418 Maple Ridge Lane</li>
      <li class="plain">Brookvale, NC 27514</li>
      <li>
        <svg class="icon" viewBox="0 0 14 14"><path d="M3 1 L5 4 L4 5.5 Q6 9 8.5 10 L10 9 L13 11 L11.5 13 Q5 13 1 3 Z" fill="var(--orange)"/></svg>
        555-214-7630
      </li>
      <li>
        <svg class="icon" viewBox="0 0 14 14"><rect x="3" y="1" width="8" height="4" fill="var(--orange)"/><rect x="1" y="5" width="12" height="7" rx="1" fill="var(--orange)"/><rect x="3" y="7" width="8" height="2" fill="var(--white)"/></svg>
        555-214-8842
      </li>
      <li>
        <svg class="icon" viewBox="0 0 14 14"><rect x="1" y="3" width="12" height="8" fill="var(--orange)"/><path d="M1 3 L7 8 L13 3" stroke="var(--white)" stroke-width="1.2" fill="none"/></svg>
        daltonpower@brightmail-example.net
      </li>
    </ul>

    <div class="back-name">Dalton Power<br>Supply, Inc.</div>

    <svg class="bottom-band" width="700" height="70" viewBox="0 0 700 70">
      <defs>
        <linearGradient id="bandFill" x1="0" y1="0" x2="0" y2="1">
          <stop offset="0" stop-color="var(--orange-light)"/>
          <stop offset="1" stop-color="var(--orange)"/>
        </linearGradient>
      </defs>
      <polygon points="0,0 700,0 700,70 0,70" fill="none"/>
      <polygon points="0,40 260,40 245,70 0,70" fill="url(#bandFill)"/>
      <polygon points="272,40 700,40 700,70 257,70" fill="url(#bandFill)" opacity="0.95"/>
    </svg>
  </section>
</body>
</html>
```